RZO Design tag

Looking to design a tag for our new hat & glove brand RZO Design. These are winter hats & gloves. Long story short these are lower cost/retail items but I'm trying to convey higher quality goods through a nice tag. I’ve attached a tag of another brand we have to give you a general idea of what I’d be looking for- but again for our new brand RZO Design.
I’m thinking we can do one general design- and then do it in 4 different color schemes: First one mimicking the attachment’s colors for ladies items- so a few different shades of pink. Then 2nd color scheme a darker more masculine color tone for mens or unisex items- maybe blue/dark blue, and then a 3rd color scheme for kids items that is more vibrant/kid like colors. Last one red & green for some Christmas items we do.
A few things:
• Trying to make the tags look classy as possible
• The tag will need to measure 2.25” high x 2” wide. The top little bit would have to be space left blank for a hole punch- just like on the attached sample tag. But again the tags designed would need to be 2.25" tall x 2" wide so not the same shape as the sample tag.
• For item name you can just put “Knit Hat” for the generic tag item name (in place of what says on the same “Chenille Slipper Bootie”). Please try to keep the writing a nice font similar to what is on this tag- again trying to have a classy tag look
• On the bottom center (In place of Made in China) it would just need to say “One Size” in standard font
Hope this helps & thank you
Target Market(s)
People buying winter hats & gloves
Industry/Entity Type
Retail- winter hats & gloves
Look and feel

```html
<!DOCTYPE html>
<html lang="en">
<head>
<meta charset="utf-8">
<title>Knit Hat Tags – Four Colourways</title>
<link href="https://fonts.googleapis.com/css2?family=Yellowtail&family=Montserrat:wght@600&display=swap" rel="stylesheet">
<style>
  :root {
    --page: #ffffff;
    --pink-light: #fbc6e3;
    --pink-mid: #f78ac6;
    --pink-deep: #e5007e;
    --xmas-green: #2d520e;
    --xmas-bright: #027a17;
    --xmas-red: #c7070f;
    --xmas-scarlet: #ff1c36;
    --navy-light: #243a5e;
    --navy-mid: #1d2f4e;
    --navy-dark: #17233b;
    --navy-ink: #00225a;
    --kid-orange: #ef5034;
    --kid-red: #e6262a;
    --kid-amber: #fbb21a;
    --kid-yellow: #f4e920;
    --kid-teal: #4c94ac;
    --white: #ffffff;
  }
  * { box-sizing: border-box; margin: 0; padding: 0; }
  html, body { width: 1200px; height: 1200px; overflow: hidden; background: var(--page); }
  .sheet { position: relative; width: 1200px; height: 1200px; }

  .tag { position: absolute; width: 360px; height: 401px; overflow: hidden; }
  .tag--ladies { left: 128px; top: 169px; }
  .tag--holiday { left: 694px; top: 169px; }
  .tag--mens { left: 120px; top: 677px; }
  .tag--kids { left: 692px; top: 671px; }

  .tag__pattern { position: absolute; inset: 0; }
  .tag--ladies .tag__pattern {
    background: radial-gradient(circle at 55% 50%, #fde0ea 0%, var(--pink-light) 35%, var(--pink-mid) 100%);
  }
  .tag--holiday .tag__pattern {
    background: linear-gradient(160deg, var(--xmas-green) 0%, var(--xmas-bright) 30%, var(--xmas-red) 55%, var(--xmas-scarlet) 75%, var(--xmas-green) 100%);
  }
  .tag--mens .tag__pattern {
    background: linear-gradient(170deg, var(--navy-light) 0%, var(--navy-mid) 50%, var(--navy-light) 100%);
  }
  .tag--kids .tag__pattern {
    background: linear-gradient(160deg, var(--kid-red) 0%, var(--kid-orange) 30%, var(--kid-amber) 55%, var(--kid-orange) 80%, var(--kid-red) 100%);
  }

  .tag__hole {
    position: absolute; left: 50%; top: 15px; width: 28px; height: 28px;
    margin-left: -14px; border-radius: 50%; background: var(--page);
  }

  .tag__name {
    position: absolute; font-family: "Yellowtail", cursive; line-height: 1;
    color: var(--white); -webkit-text-stroke: 3px var(--stroke); paint-order: stroke fill;
    transform: rotate(-6deg);
  }
  .tag__name--knit { left: 58px; top: 80px; font-size: 158px; }
  .tag__name--hat { left: 120px; top: 196px; font-size: 122px; }

  .tag__size {
    position: absolute; left: 0; right: 0; bottom: 4px; text-align: center;
    font-family: "Montserrat", sans-serif; font-weight: 600; font-size: 27px; letter-spacing: 0.5px;
    color: var(--white);
  }

  .tag--ladies { --stroke: var(--pink-deep); }
  .tag--ladies .tag__size { -webkit-text-stroke: 1px var(--pink-deep); paint-order: stroke fill; bottom: 2px; }
  .tag--holiday { --stroke: var(--xmas-red); }
  .tag--holiday .tag__size { bottom: 12px; }
  .tag--mens { --stroke: var(--white); }
  .tag--mens .tag__name { color: var(--navy-ink); }
  .tag--mens .tag__size { color: var(--navy-ink); -webkit-text-stroke: 1px var(--white); paint-order: stroke fill; bottom: 8px; }
  .tag--kids { --stroke: var(--kid-red); }
  .tag--kids .tag__size { bottom: 2px; }
</style>
</head>
<body>
<main class="sheet">
  <section class="tag tag--ladies">
    <div class="tag__pattern" role="img" aria-label="Abstract flowing pattern in soft shades of pink"></div>
    <div class="tag__hole"></div>
    <p class="tag__name tag__name--knit">Knit</p>
    <p class="tag__name tag__name--hat">Hat</p>
    <p class="tag__size">One Size</p>
  </section>

  <section class="tag tag--holiday">
    <div class="tag__pattern" role="img" aria-label="Abstract liquid camouflage pattern in red and green"></div>
    <div class="tag__hole"></div>
    <p class="tag__name tag__name--knit">Knit</p>
    <p class="tag__name tag__name--hat">Hat</p>
    <p class="tag__size">One Size</p>
  </section>

  <section class="tag tag--mens">
    <div class="tag__pattern" role="img" aria-label="Abstract liquid contour pattern in navy tones"></div>
    <div class="tag__hole"></div>
    <p class="tag__name tag__name--knit">Knit</p>
    <p class="tag__name tag__name--hat">Hat</p>
    <p class="tag__size">One Size</p>
  </section>

  <section class="tag tag--kids">
    <div class="tag__pattern" role="img" aria-label="Abstract liquid pattern in orange, red, yellow and teal"></div>
    <div class="tag__hole"></div>
    <p class="tag__name tag__name--knit">Knit</p>
    <p class="tag__name tag__name--hat">Hat</p>
    <p class="tag__size">One Size</p>
  </section>
</main>
</body>
</html>
```